Business Card Design Project

I need a business card design for my freelance solo makeup artistry business in Melbourne, Australia called Rosa Fennimore. My freelance business specialises in bridal and special occassions makeup.

I like the idea of having Rosa Fennimore in pink as its a feminine and soft colour. I would like a very clean, classy and simple (with an element of fun if that's possible) design. I would consider the business name to be in gloss with an otherwise matte finish.

Underneath the business name, I would like "Makeup by Tara Quillend"

I do not want any bridal related graphics.

Target Market(s)

Young females with a disposable income from ages 20-40 and females getting married who will dictate who does mother of bride makeup ages 40-70.

Industry/Entity Type

Business

Requirements
Must have
• "Makeup by Tara Quillend"

Ph: 0432 615 204
E: rosafennimore@examplemail.com
ABN: 58902147635
Nice to have
• I think I would like a mini business cards which is more slimline. I do like the colours of pink, white and grey but open to suggestions.
Should not have
• Bridal related graphics

```html
<!DOCTYPE html>
<html lang="en">
<head>
<meta charset="utf-8">
<title>Rosa Fennimore – Business Card</title>
<link href="https://fonts.googleapis.com/css2?family=Tinos:ital,wght@0,400;0,700;1,400;1,700&display=swap" rel="stylesheet">
<style>
  :root {
    --paper: #ffffff;
    --ink: #111111;
    --brand-pink: #d2519a;
    --band-lilac: #efeaf6;
    --band-edge: #d9d4e2;
    --rule-dark: #1a1a1a;
    --art-warm: #f1dde2;
    --art-warm-soft: #f8eef1;
    --art-cool: #dfe4ee;
    --art-cool-soft: #eef1f6;
  }
  * { margin: 0; padding: 0; box-sizing: border-box; }
  html, body {
    width: 1200px; height: 777px; overflow: hidden;
    background: var(--paper);
  }
  .card {
    position: relative;
    width: 1200px; height: 777px;
    background: var(--paper);
    font-family: "Tinos", "Times New Roman", serif;
    color: var(--ink);
  }
  .top-rule {
    position: absolute; left: 40px; top: 0;
    width: 1000px; height: 4px;
    background: var(--rule-dark);
  }
  .art { position: absolute; }
  .art--palette {
    left: 72px; top: 12px; width: 228px; height: 178px;
    background: linear-gradient(135deg, var(--art-warm), var(--art-warm-soft));
  }
  .art--brush-left {
    left: 290px; top: 36px; width: 152px; height: 84px;
    background: linear-gradient(90deg, var(--art-cool-soft), var(--art-cool));
  }
  .art--brush-right {
    left: 885px; top: 36px; width: 165px; height: 84px;
    background: linear-gradient(90deg, var(--art-cool-soft), var(--art-cool));
  }
  .brand-name {
    position: absolute; left: 450px; top: 72px;
    width: 380px; text-align: center;
    white-space: nowrap;
    font-size: 50px; font-weight: 400; line-height: 60px;
    color: var(--brand-pink);
  }
  .tagline {
    position: absolute; left: 0; top: 192px;
    width: 1190px; text-align: center;
    font-size: 38px; font-weight: 700; font-style: italic;
    white-space: nowrap;
  }
  .services-band {
    position: absolute; left: 0; top: 275px;
    width: 1200px; height: 100px;
    background: var(--band-lilac);
    border-top: 2px solid var(--band-edge);
    border-bottom: 2px solid var(--band-edge);
    text-align: center;
    padding-top: 8px;
    padding-right: 20px;
    font-size: 33px; line-height: 43px;
  }
  .contact {
    position: absolute; left: 118px; top: 450px;
    font-size: 31px; line-height: 48px;
  }
  .contact-row { display: flex; white-space: pre; }
  .contact-label { font-style: italic; width: 112px; }
  .location {
    position: absolute; left: 118px; top: 638px;
    font-size: 32px; font-style: italic;
  }
</style>
</head>
<body>
  <main class="card">
    <div class="top-rule"></div>
    <div class="art art--palette" role="img" aria-label="Illustration of an open makeup palette"></div>
    <div class="art art--brush-left" role="img" aria-label="Illustration of a makeup brush"></div>
    <div class="art art--brush-right" role="img" aria-label="Illustration of a makeup brush"></div>

    <h1 class="brand-name">Rosa Fennimore</h1>
    <p class="tagline">Makeup by Tara Quillend</p>

    <section class="services-band">
      <p>Bridal and special<br>occassions makeup.</p>
    </section>

    <section class="contact">
      <p class="contact-row"><span class="contact-label">Phone  :</span><span>0432 615 204</span></p>
      <p class="contact-row"><span class="contact-label">E-mail :</span><span>rosafennimore@examplemail.com</span></p>
      <p class="contact-row"><span class="contact-label">ABN   :</span><span> 58902147635</span></p>
    </section>

    <p class="location">Melbourne, Australia</p>
  </main>
</body>
</html>
```